Warranty Card Design for Mattress Brand

We would like to design a warranty card for our mattresses,
it consists of 2 pages in one card (front and back) to be neatly showing our warranty details/text , our logo , our website, address and telephone clearly.

Target Market(s)

household

Font styles to use
Serif
Script

Colors
3277b5
33a6d7
85cae6
0492cd
3176b5
0355a3
85abd2
cee9f5
85acd3

Requirements
Must have
• a nice warranty logo
Nice to have
• a nice warranty logo with a neat text and clear layout, colors have to be related to the logo

```html
<!DOCTYPE html>
<html lang="en">
<head>
<meta charset="utf-8">
<title>Dreamrest Warranty Card</title>
<link rel="stylesheet" href="https://fonts.googleapis.com/css2?family=Cormorant+Garamond:wght@500&family=Josefin+Slab:wght@300;400&family=Open+Sans:ital,wght@0,400;0,700;1,400;1,700&display=swap">
<style>
  :root {
    --backdrop: #5f8096;
    --card-light: #ffffff;
    --card-tint: #cfe7f4;
    --brand: #4a6fb8;
    --brand-dark: #3a5a9c;
    --ink: #2b3240;
    --ink-soft: #4a5262;
    --bullet: #3176b5;
  }
  * { box-sizing: border-box; margin: 0; padding: 0; }
  html, body { width: 1200px; height: 696px; overflow: hidden; }
  body {
    background: var(--backdrop);
    font-family: "Open Sans", sans-serif;
    position: relative;
  }
  .card {
    position: absolute;
    top: 168px;
    width: 560px;
    height: 360px;
    background: radial-gradient(ellipse at 50% 45%, var(--card-light) 0%, #eaf5fb 45%, var(--card-tint) 100%);
    box-shadow: 0 6px 18px rgba(0,0,0,0.25);
    overflow: hidden;
  }
  .card--back { left: 26px; padding: 20px 22px; }
  .card--front { left: 614px; }

  /* Back: warranty text */
  .back-columns { display: flex; gap: 22px; height: 100%; }
  .terms { flex: 1 1 52%; font-size: 7.2px; line-height: 1.55; color: var(--ink); font-style: italic; }
  .care  { flex: 1 1 48%; font-size: 7.2px; line-height: 1.55; color: var(--ink); font-style: italic; display: flex; flex-direction: column; }
  .terms p { margin-bottom: 0; }
  .terms .indent { padding-left: 10px; }
  .section-title { text-decoration: underline; margin-top: 8px; padding-left: 10px; }
  .exclusions { list-style: none; display: flex; flex-wrap: wrap; column-gap: 10px; }
  .exclusions li::before, .care-list li::before {
    content: ""; display: inline-block; width: 4px; height: 4px; border-radius: 50%;
    background: var(--bullet); margin-right: 4px; vertical-align: middle;
  }
  .company { font-weight: 700; margin-top: 4px; }
  .care-heading { font-weight: 700; margin-bottom: 3px; }
  .care-list { list-style: none; }
  .care-list li { margin-bottom: 3px; }
  .fields { display: flex; justify-content: space-between; margin-top: 16px; padding: 0 4px; }
  .mini-brand { margin-top: auto; align-self: center; text-align: center; color: var(--brand); }
  .mini-brand .name { font-family: "Cormorant Garamond", serif; font-size: 22px; font-weight: 500; font-style: normal; line-height: 1; }
  .mini-brand .site { font-family: "Josefin Slab", serif; font-size: 7px; font-style: normal; letter-spacing: .5px; }

  /* Front: brand face */
  .front-brand { position: absolute; top: 78px; left: 0; right: 0; text-align: center; color: var(--brand); }
  .wordmark { display: inline-flex; align-items: center; gap: 12px; }
  .wordmark-dot { width: 22px; height: 22px; border-radius: 50%; background: var(--brand); }
  .wordmark-name { font-family: "Cormorant Garamond", serif; font-weight: 500; font-size: 76px; line-height: 1; }
  .tagline { font-family: "Josefin Slab", serif; font-weight: 300; font-size: 17px; letter-spacing: 6px; margin-top: 6px; }
  .contact-line { display: flex; justify-content: center; align-items: center; gap: 14px; margin-top: 14px;
    font-family: "Josefin Slab", serif; font-size: 16px; color: var(--brand-dark); }
  .contact-line svg, .address svg { width: 16px; height: 16px; }
  .phone { display: inline-flex; align-items: center; gap: 6px; }
  .address { position: absolute; left: 0; right: 0; bottom: 42px; display: flex; justify-content: center; align-items: center; gap: 8px;
    font-family: "Josefin Slab", serif; font-size: 17px; color: var(--ink); }
</style>
</head>
<body>

<section class="card card--back" aria-label="Warranty card, back">
  <div class="back-columns">
    <div class="terms">
      <p class="indent">Congratulations on your new DREAMREST mattress.</p>
      <p>We always strive to provide you with the most comfortable and healthy sleep by offering you the highest product quality and durability.</p>
      <p class="indent">Our company was awarded the ISO 9001 accreditation certificate for the quality of its Mattress Production.</p>
      <p class="indent">By implementing the ISO 9001 quality management system, we assure our customers that the products and the services we provide will meet their expectations.</p>
      <p class="indent">Our products are guaranteed against defects in workmanship and material. In case of defect, we shall repair or replace, at our discretion, the defective component.</p>
      <p>Please keep this card in a safe place. Should you face any problems, please contact our service department.</p>
      <p class="section-title">This limited Mattress Warranty applies to the following Defects:</p>
      <p class="indent">Coils or wires that are broken or piercing through fabric.</p>
      <p class="indent">Sagging that measures 3cm or greater (being properly measured) only if the mattress has been continuously supported by appropriate and solid foundation.</p>
      <p class="section-title" style="margin-top:2px">This limited Mattress Warranty does not cover the following:</p>
      <ul class="exclusions">
        <li>Comfort preference</li>
        <li>Fabric Stains, soiling or burns</li>
        <li>Body impressions of less than 3cm</li>
        <li>Damage to the mattress due to abuse</li>
        <li>Bent Perimeter border rods due to moving or bending the mattress</li>
        <li>Size allowance of +/- 2cm</li>
        <li>Bed Bugs and Dust Mites</li>
      </ul>
      <p>Mattress Odor: as in any upholstery, new mattress may have odor that will fade with time.</p>
      <p>For Latex and Memory Foam mattresses: normal change in softness and recovery time in these materials with time.</p>
      <p>Transportation and Inspection Costs</p>
      <p class="company">Hadi Saleh and Sons</p>
      <p>Cedar Park, Mill Road, Aley, Lebanon</p>
      <p>+961 1 555 014</p>
    </div>
    <div class="care">
      <p class="care-heading">To ensure you get maximum comfort and support, please follow the following instructions:</p>
      <ul class="care-list">
        <li>Make sure the bed base foundation is in good condition and well ventilated.</li>
        <li>Turn/Flip your mattress every 3 months to maximize its comfort and lifespan.</li>
        <li>Avoid exposing the mattress to the sun; air it in a passage area instead.</li>
        <li>In case of possibility of liquids dripping on the mattress, consider covering it with a mattress protection pad.</li>
        <li>Do not worry if the mattress feels slightly firmer than anticipated; within weeks of usage, the interior will soften and initial stiffness will be removed.</li>
      </ul>
      <div class="fields">
        <span>Invoice Number</span>
        <span>Warranty Period</span>
        <span>Date</span>
      </div>
      <div class="mini-brand">
        <div class="name">Dreamrest</div>
        <div class="site">www.hadisalehandsons.com</div>
      </div>
    </div>
  </div>
</section>

<section class="card card--front" aria-label="Warranty card, front">
  <div class="front-brand">
    <div class="wordmark">
      <span class="wordmark-dot"></span>
      <span class="wordmark-name">Dreamrest</span>
    </div>
    <div class="tagline">MATTRESSES &amp; PILLOWS</div>
    <div class="contact-line">
      <span>www.hadisalehandsons.com</span>
      <span class="phone">
        <svg viewBox="0 0 16 16" aria-hidden="true"><circle cx="8" cy="8" r="7" fill="none" stroke="currentColor" stroke-width="1.2"/><path d="M5.6 4.6l1.2-.2.7 1.6-.8.7a5 5 0 0 0 2.6 2.6l.7-.8 1.6.7-.2 1.2c-3 .5-6.2-2.7-5.8-5.8z" fill="currentColor"/></svg>
        +961 1 555 014
      </span>
    </div>
  </div>
  <div class="address">
    <svg viewBox="0 0 16 16" aria-hidden="true"><circle cx="8" cy="8" r="7" fill="none" stroke="currentColor" stroke-width="1.2"/><path d="M8 3.8a2.6 2.6 0 0 0-2.6 2.6C5.4 8.4 8 11.6 8 11.6s2.6-3.2 2.6-5.2A2.6 2.6 0 0 0 8 3.8zm0 3.6a1 1 0 1 1 0-2 1 1 0 0 1 0 2z" fill="currentColor"/></svg>
    <span>Cedar Park, Mill Road, Aley, Lebanon</span>
  </div>
</section>

</body>
</html>
```